Alaska Law Firm Needs a Sticker Design

We need a design for stickers to put on already-printed brochures. We mail the brochures to potential clients so they can learn more about accident-induced injuries, insurance claims, legal representation, and our own law firm.

One of our lawyers wrote a book that provides a helpful overview of personal injury claims. We are offering this book for free to anyone who calls and requests it. Therefore, the sticker design should include one of the following phrases, or something very similar:
a) "Still have questions? Call and request our book-- for free!"
b) "Still have questions about auto accident claims? Call and request our book today."
c) "Still have questions about filing a claim? Call and request a free copy of our book."
d) "Still have questions? Call us today to request a free copy of our book, Clear Lanes Ahead."
e) "To learn more about automobile accidents and insurance, call today and request a free copy of our book."

The sticker should be approximately 3"x3" and may be a circle, square, rectangle, or ellipsis. The sticker will be placed on the back of the folder, which is light blue. We would like the sticker to match the color scheme of our website and the folder.

I will upload an image of the book cover as soon as I obtain it.

Industry/Entity Type

Law Firm

Font styles to use
Serif
Sans Serif

Requirements
Should not have
• Bright colors that aren't already used in the folder design. e.g. no bright orange, pink, chartreuse, turquoise, yellow, red.

```html
<!DOCTYPE html>
<html lang="en">
<head>
<meta charset="utf-8">
<title>Free Book Sticker – Clear Lanes Ahead</title>
<link rel="stylesheet" href="https://fonts.googleapis.com/css2?family=Open+Sans:ital,wght@0,300;0,400;0,800;1,600&display=swap">
<style>
  :root {
    --navy: #0f4170;
    --navy-deep: #0b355d;
    --navy-soft: #1d5285;
    --paper: #ffffff;
    --shadow: #04111f;
  }
  html, body {
    margin: 0;
    padding: 0;
    width: 1200px;
    height: 1200px;
    overflow: hidden;
    background: var(--paper);
  }
  .sticker {
    display: block;
    width: 1200px;
    height: 1200px;
  }
  .sticker text { font-family: "Open Sans", Arial, sans-serif; }
  .question { fill: var(--paper); font-size: 33px; font-weight: 400; }
  .call-line { fill: var(--navy); font-size: 54px; font-weight: 300; }
  .free-word { fill: var(--navy); font-size: 196px; font-weight: 800; }
  .book-copy { fill: var(--paper); font-size: 38px; font-weight: 300; }
  .book-title { fill: var(--paper); font-size: 60px; font-weight: 600; font-style: italic; }
  .divider { stroke: var(--paper); stroke-width: 2; }
</style>
</head>
<body>
<svg class="sticker" viewBox="0 0 900 900" xmlns="http://www.w3.org/2000/svg" role="img" aria-label="Sticker: Still have questions about filing a claim? Call and request a free copy of our book, Clear Lanes Ahead">
  <defs>
    <clipPath id="disc-clip">
      <circle cx="450" cy="450" r="428"/>
    </clipPath>
    <filter id="band-shadow" x="-10%" y="-100%" width="120%" height="300%">
      <feGaussianBlur stdDeviation="4"/>
    </filter>
    <linearGradient id="book-area-fill" x1="0" y1="0" x2="0" y2="1">
      <stop offset="0" stop-color="var(--navy-soft)"/>
      <stop offset="1" stop-color="var(--navy)"/>
    </linearGradient>
  </defs>

  <!-- outer white ring with rim -->
  <circle class="sticker-rim" cx="450" cy="450" r="446" fill="var(--paper)" stroke="var(--navy)" stroke-width="5"/>

  <g clip-path="url(#disc-clip)">
    <rect class="disc-top" x="0" y="0" width="900" height="900" fill="var(--navy)"/>
    <rect class="disc-bottom" x="0" y="585" width="900" height="315" fill="var(--navy-deep)"/>

    <!-- shadow under white band -->
    <rect class="band-shadow" x="55" y="584" width="790" height="24" fill="var(--shadow)" opacity="0.95" filter="url(#band-shadow)"/>

    <!-- white band -->
    <rect class="message-band" x="0" y="390" width="900" height="195" fill="var(--paper)"/>

    <!-- lower grid lines -->
    <line class="divider" x1="105" y1="680" x2="900" y2="680"/>
    <line class="divider" x1="710" y1="588" x2="710" y2="770"/>
  </g>

  <!-- illustration area -->
  <rect class="book-illustration" x="190" y="100" width="520" height="232" rx="12" fill="url(#book-area-fill)" role="img" aria-label="Open book illustration"/>

  <text class="question" x="450" y="370" text-anchor="middle">Still have questions about filing a claim?</text>

  <text class="call-line" x="335" y="466" text-anchor="end">Call and</text>
  <text class="call-line" x="335" y="533" text-anchor="end">Request a</text>
  <text class="free-word" x="364" y="549" textLength="442" lengthAdjust="spacingAndGlyphs">FREE</text>

  <text class="book-copy" x="450" y="652" text-anchor="middle">copy of our book</text>

  <text class="book-title" x="450" y="758" text-anchor="middle">CLEAR LANES</text>
  <text class="book-title" x="450" y="830" text-anchor="middle">AHEAD</text>
</svg>
</body>
</html>
```